Corlith Australia Pty Ltd

I require professional business cards with our company logo. We would like something that looks sharp and unique. I have attached the logo for our business, which is an industrial electrical contracting company. But this does not need to be shown on the cards.

Requirements
Must have
• The design must be double sided and needs to have one side with our logo only and the other side with our details.
Should not have
• We do not want any lightening bolts on the designs as this is very common.

```html
<!DOCTYPE html>
<html lang="en">
<head>
<meta charset="utf-8">
<title>Corlith Australia Pty Ltd – Business Cards</title>
<link href="https://fonts.googleapis.com/css2?family=Arimo:wght@400;700&display=swap" rel="stylesheet">
<style>
  :root {
    --backdrop: #e4e2de;
    --card-black: #0d0d0d;
    --card-white: #f4f4f2;
    --gold: #c9a24a;
    --ink: #3a3a3a;
    --shadow: rgba(0,0,0,0.22);
  }
  * { margin: 0; padding: 0; box-sizing: border-box; }
  html, body {
    width: 1200px; height: 900px; overflow: hidden;
    background: var(--backdrop);
    font-family: "Arimo", Arial, sans-serif;
  }
  .sheet {
    width: 1200px; height: 900px;
    display: flex; flex-direction: column; align-items: center; justify-content: center;
    gap: 40px;
  }
  .card {
    position: relative;
    width: 680px; height: 380px;
    box-shadow: 0 10px 28px var(--shadow);
    overflow: hidden;
  }

  /* Front: logo side */
  .card--front {
    background: var(--card-black);
    display: flex; flex-direction: column; align-items: center; justify-content: center;
  }
  .wordmark { color: var(--gold); font-weight: 400; text-align: center; line-height: 1; }
  .wordmark__name { display: block; font-size: 82px; letter-spacing: 4px; }
  .wordmark__suffix { display: block; font-size: 21px; letter-spacing: 14px; margin-top: 8px; padding-left: 14px; }
  .front-web {
    margin-top: 44px; color: var(--gold);
    font-size: 16px; letter-spacing: 4px;
  }

  /* Back: details side */
  .card--back { background: var(--card-white); }
  .brand {
    position: absolute; left: 44px; top: 56px;
    display: flex; align-items: center; gap: 20px;
  }
  .brand__dot {
    width: 84px; height: 84px; border-radius: 50%;
    background: var(--gold);
    flex: none;
  }
  .brand .wordmark { text-align: left; }
  .brand .wordmark__name { font-size: 46px; letter-spacing: 2px; }
  .brand .wordmark__suffix { font-size: 12px; letter-spacing: 6.5px; margin-top: 6px; padding-left: 2px; }

  .address {
    position: absolute; right: 36px; top: 62px; width: 196px;
    font-size: 14px; line-height: 1.6; color: var(--ink); text-align: left;
    font-style: normal;
  }
  .address__web { color: var(--gold); margin-top: 10px; display: block; }

  .name-band {
    position: absolute; left: 0; right: 0; top: 186px; height: 56px;
    background: var(--card-black);
    display: flex; align-items: center; gap: 12px; padding-left: 44px;
  }
  .name-band__name { color: var(--gold); font-weight: 700; font-size: 25px; letter-spacing: 0.5px; }
  .name-band__role { color: var(--gold); font-size: 18px; }

  .contacts {
    position: absolute; left: 44px; top: 262px;
    list-style: none; display: flex; flex-direction: column; gap: 9px;
  }
  .contacts__item { display: flex; align-items: center; gap: 14px; font-size: 17px; color: var(--ink); }
  .contacts__icon {
    width: 28px; height: 28px; border: 1.6px solid var(--gold); border-radius: 50%;
    display: flex; align-items: center; justify-content: center;
  }
  .contacts__icon svg { width: 15px; height: 15px; }
</style>
</head>
<body>
<main class="sheet">

  <section class="card card--front" aria-label="Card front">
    <div class="wordmark">
      <span class="wordmark__name">CORLITH</span>
      <span class="wordmark__suffix">AUSTRALIA PTY LTD</span>
    </div>
    <p class="front-web">www.corlithaustralia.com.au</p>
  </section>

  <section class="card card--back" aria-label="Card back">
    <div class="brand">
      <span class="brand__dot"></span>
      <div class="wordmark">
        <span class="wordmark__name">CORLITH</span>
        <span class="wordmark__suffix">AUSTRALIA PTY LTD</span>
      </div>
    </div>

    <address class="address">
      PO Box 318<br>
      Harwood NSW 2571
      <span class="address__web">www.corlithaustralia.com.au</span>
    </address>

    <div class="name-band">
      <span class="name-band__name">MARCUS HALE</span>
      <span class="name-band__role">Director</span>
    </div>

    <ul class="contacts">
      <li class="contacts__item">
        <span class="contacts__icon">
          <svg viewBox="0 0 24 24" fill="none" stroke="#c9a24a" stroke-width="2" stroke-linecap="round" stroke-linejoin="round"><path d="M5 3h4l2 5-2.5 1.5a11 11 0 0 0 6 6L16 13l5 2v4a2 2 0 0 1-2 2A16 16 0 0 1 3 5a2 2 0 0 1 2-2"/></svg>
        </span>
        02 4719 3058
      </li>
      <li class="contacts__item">
        <span class="contacts__icon">
          <svg viewBox="0 0 24 24" fill="none" stroke="#c9a24a" stroke-width="2" stroke-linecap="round"><rect x="6" y="2" width="12" height="20" rx="2"/><line x1="11" y1="18" x2="13" y2="18"/></svg>
        </span>
        0412 730 295
      </li>
      <li class="contacts__item">
        <span class="contacts__icon">
          <svg viewBox="0 0 24 24" fill="none" stroke="#c9a24a" stroke-width="2" stroke-linejoin="round"><rect x="2" y="5" width="20" height="14" rx="1"/><path d="M2 6l10 7 10-7"/></svg>
        </span>
        marcus@corlithaustralia.com.au
      </li>
    </ul>
  </section>

</main>
</body>
</html>
```